依頼詳細
12月の年末繁忙期に合わせて、新聞折込を実施する予定です。ただ、おコメの麺の説明が難しく消費者には伝わりにくいため、純粋にちゃんぽんや台湾風まぜそばを全面に打ち出して当社に来店してもらい、結果的に米粉麺だったくらいの主張でいいと思っています。チラシの下部に100円キャッシュバック券をつけたいと考えています。(期限は2023年2月末)
記載項目
こむぎ茶屋 しずくや みずほ灯籠館店 (道の駅みずほ灯籠館内フードコート)
住所 長岡市桜井町318 TEL090-6978-5739
営業時間10:00~19:00

とろみちゃんぽん 880円
とろみちゃんぽん旨辛味噌のせ 910円
台湾風まぜそば 910円
サイズ
A4
ページ数
片面
希望イメージ
シンプル 複雑
単色 カラフル
暗い 明るい
日常 高級
遊び心 厳粛
未来的 伝統的
女性的 男性的
希望する色
黄・オレンジ系
納品ファイル
• 高解像度JPG (.jpg)

はじめてみた人が感じるインパクトがあり、色彩もよかったです。

毎回たくさんの応募ありがとうございます。
結果的に非常に満足しておりますので、これからも依頼したいと思います。
よろしくお願いします。

```html
<!DOCTYPE html>
<html lang="ja">
<head>
<meta charset="utf-8">
<title>こむぎ茶屋 しずくや 年末年始チラシ</title>
<link href="https://fonts.googleapis.com/css2?family=Dela+Gothic+One&family=Noto+Sans+JP:wght@500;700;900&display=swap" rel="stylesheet">
<style>
:root{
  --red:#d8231a;
  --deep-red:#8e1a12;
  --yellow:#ffd91c;
  --orange:#f6a316;
  --ink:#231815;
  --white:#ffffff;
}
*{margin:0;padding:0;box-sizing:border-box}
html,body{width:849px;height:1200px;overflow:hidden}
body{font-family:"Noto Sans JP",sans-serif;color:var(--ink);background:var(--yellow)}
.flyer{position:relative;width:849px;height:1200px;overflow:hidden;
  background:linear-gradient(160deg,var(--yellow) 40%,var(--orange) 100%)}
.backdrop{position:absolute;inset:0}
.top-banner{position:absolute;left:0;top:0;width:100%;height:55px;background:var(--deep-red);
  display:flex;align-items:center;justify-content:center;
  font-family:"Dela Gothic One",sans-serif;font-size:26px;color:var(--yellow);letter-spacing:1px;z-index:3}
.top-banner em{font-style:normal;color:var(--white)}
.photo{position:absolute;border-radius:50%;box-shadow:0 6px 14px rgba(0,0,0,.3);z-index:1}
.photo-champon{left:290px;top:62px;width:262px;height:180px;
  background:radial-gradient(circle at 50% 45%,#f8f2e0 0%,#e9dcb8 55%,#c7b07c 80%,#2b2522 82%)}
.photo-miso{left:524px;top:258px;width:270px;height:205px;
  background:radial-gradient(circle at 50% 45%,#f3e6c8 0%,#e0c38d 40%,#c98b45 60%,#3a2a22 82%)}
.photo-mazesoba{left:150px;top:356px;width:370px;height:292px;
  background:radial-gradient(circle at 50% 45%,#f2b33a 0%,#b4562a 30%,#6e3019 60%,#1e1815 82%)}
.headline{position:absolute;writing-mode:vertical-rl;font-family:"Dela Gothic One",sans-serif;line-height:1;z-index:2}
.headline-left{left:20px;top:80px;font-size:72px;color:var(--yellow);letter-spacing:6px}
.headline-right{right:20px;top:66px;font-size:60px;color:var(--red);letter-spacing:2px;
  -webkit-text-stroke:4px var(--white);paint-order:stroke fill}
.menu-item{position:absolute;font-weight:900;line-height:1.2;color:var(--ink);z-index:2}
.menu-item .price{display:block;font-family:"Dela Gothic One",sans-serif;font-size:38px;color:var(--red);line-height:1.1}
.menu-item .price small{font-size:22px}
.item-champon{left:300px;top:246px;font-size:21px}
.item-miso{left:540px;top:470px;font-size:19px}
.item-mazesoba{left:552px;top:592px;font-size:19px}
.catch{position:absolute;font-weight:900;line-height:1.15;z-index:2}
.catch-veg{left:610px;top:66px;writing-mode:vertical-rl;font-size:20px;color:var(--deep-red);transform:rotate(-8deg)}
.catch-meat{left:136px;top:340px;writing-mode:vertical-rl;font-size:16px;color:var(--white);
  background:var(--deep-red);padding:8px 4px}
.catch-texture{left:590px;top:664px;font-size:16px;font-weight:700;color:var(--ink);transform:rotate(-8deg)}
.coupon{position:absolute;left:265px;top:700px;width:435px;height:405px;background:var(--white);
  border:4px dashed var(--red);outline:6px solid var(--white);text-align:center;z-index:3}
.coupon-lead{background:var(--red);color:var(--white);font-weight:900;font-size:24px;padding:8px 0}
.coupon-amount{font-family:"Dela Gothic One",sans-serif;color:var(--red);font-size:136px;line-height:1;margin-top:16px}
.coupon-amount small{font-size:60px}
.coupon-title{font-family:"Dela Gothic One",sans-serif;color:var(--red);font-size:42px;line-height:1.1;margin-top:6px}
.coupon-expiry{font-weight:700;font-size:17px;margin-top:12px}
.coupon-notes{font-size:12px;font-weight:500;margin-top:8px;line-height:1.5}
.person{position:absolute;left:700px;top:750px;width:149px;height:370px;
  background:linear-gradient(180deg,#f2d2b6 0%,#d9a07c 45%,#f6a316 100%);border-radius:80px 80px 0 0;z-index:1}
.footer{position:absolute;left:0;bottom:0;width:100%;height:80px;background:var(--white);
  border-top:6px solid var(--red);display:flex;align-items:center;padding:0 18px;gap:14px;z-index:3}
.shop-mark{width:30px;height:30px;border-radius:50%;background:var(--red);flex:none}
.shop-name{font-weight:900;font-size:24px;color:var(--deep-red);white-space:nowrap}
.shop-info{font-size:12px;font-weight:700;line-height:1.4;white-space:nowrap}
</style>
</head>
<body>
<div class="flyer">
  <svg class="backdrop" width="849" height="1200" viewBox="0 0 849 1200" aria-hidden="true">
    <polygon points="0,55 330,55 240,1120 0,1120" fill="var(--red)"/>
  </svg>

  <div class="top-banner">年末も年始も<em>こむぎ茶屋「しずくや」</em>でキマリ！</div>

  <div class="photo photo-champon" role="img" aria-label="とろみちゃんぽんの写真"></div>
  <div class="photo photo-miso" role="img" aria-label="とろみちゃんぽん旨辛味噌のせの写真"></div>
  <div class="photo photo-mazesoba" role="img" aria-label="台湾風まぜそばの写真"></div>
  <div class="person" role="img" aria-label="麺を食べる女性のイラスト"></div>

  <div class="headline headline-left">年明けは、台湾風まぜそば！</div>
  <div class="headline headline-right">年越しは、ちゃんぽん！</div>

  <div class="catch catch-veg">国産野菜<br>たっぷり！</div>
  <div class="catch catch-meat">ひき肉と野菜、魚粉の旨味！</div>
  <div class="catch catch-texture">つるつる、もちもち！</div>

  <div class="menu-item item-champon">とろみちゃんぽん<span class="price">880<small>円</small></span></div>
  <div class="menu-item item-miso">とろみちゃんぽん<br>旨辛味噌のせ<span class="price">910<small>円</small></span></div>
  <div class="menu-item item-mazesoba">台湾風まぜそば<span class="price">910<small>円</small></span></div>

  <section class="coupon">
    <p class="coupon-lead">今年一年の感謝を込めて</p>
    <p class="coupon-amount">100<small>円</small></p>
    <p class="coupon-title">キャッシュバック券</p>
    <p class="coupon-expiry">（有効期限／2023年2月末）</p>
    <p class="coupon-notes">※ご注文の際にこの券をお渡しください。<br>※お一人様一回一枚限り有効です。</p>
  </section>

  <footer class="footer">
    <span class="shop-mark"></span>
    <span class="shop-name">こむぎ茶屋「しずくや」みずほ灯籠館店</span>
    <p class="shop-info">（道の駅みずほ灯籠館内フードコート）<br>長岡市桜井町318　TEL090-4213-8062<br>営業時間10:00～19:00</p>
  </footer>
</div>
</body>
</html>
```